Recruiting ad for Caregivers and Nurses

We need a few amazing, fun, catchy, creative recruiting ads for Caregivers and Nurses to care for homecare patients on the island of Oahu, in Hawaii. We are an in home care company called Brantley Homecare. Our care services are provided 24/7, so we need staff that can work days, nights, weekdays, weekends. We need catchy fun ads to entice caregivers and nurses to call our office to inquire about jobs available. Our patients age range is from babies to seniors. We need caregivers and nurses for basic patient care (bathing, dressing, ambulating, preparing meals, medication reminders, light housekeeping) and complex patients (oxygen, tube feeding, injections, vents, wound care). Here are some bullets to consider including:
*Full-time and Part-time Positions Available (days, nights, weekdays, weekends)
*Sign-On Bonus Programs Offered up to $500
*Refer a Friend Bonus Program
*Holiday Pay
*2 Health Plans to Choose from
*Island-Wide Locations
*All PPE Provided (masks, gloves, etc)
*401K Program
*Tuition Benefits

```html
<!DOCTYPE html>
<html lang="en">
<head>
<meta charset="UTF-8">
<title>Brantley Homecare – We Are Hiring</title>
<link href="https://fonts.googleapis.com/css2?family=Archivo+Black&family=Montserrat:wght@500;600;700&family=Roboto+Condensed:wght@500;700&display=swap" rel="stylesheet">
<style>
  :root{
    --page:#cfcfcf;
    --band-grey:#e1e1e1;
    --teal:#15705f;
    --teal-line:#2aa88a;
    --teal-bright:#41d4ae;
    --teal-dark:#0f3f3b;
    --charcoal:#1f2727;
    --salmon:#f49a82;
    --ink:#111111;
    --white:#ffffff;
  }
  *{margin:0;padding:0;box-sizing:border-box;}
  html,body{width:833px;height:1200px;overflow:hidden;background:var(--page);}
  .flyer{position:absolute;left:0;top:11px;width:833px;height:1178px;overflow:hidden;background:var(--teal);font-family:"Montserrat",sans-serif;color:var(--white);}
  .hero-photo{position:absolute;left:0;top:0;width:833px;height:349px;
    background:linear-gradient(100deg,#bdbdbd 0%,#c99a80 18%,#6fc7b0 40%,#5cbfa9 62%,#1d8a86 78%,#c9a08a 90%,#b7b7b7 100%);}
  .masthead{position:absolute;left:0;top:349px;width:833px;height:194px;background:var(--band-grey);}
  .brand{position:absolute;left:106px;top:434px;width:232px;display:flex;align-items:center;justify-content:center;gap:8px;}
  .brand-mark{width:13px;height:13px;background:var(--salmon);flex:none;}
  .brand-name{font-family:"Montserrat",sans-serif;font-weight:700;font-size:17px;color:var(--teal);white-space:nowrap;}
  .masthead-rule{position:absolute;left:349px;top:373px;width:6px;height:147px;background:var(--teal);}
  .headline{position:absolute;left:403px;font-family:"Archivo Black",sans-serif;color:var(--ink);line-height:1;white-space:nowrap;}
  .headline-small{top:375px;font-size:55px;}
  .headline-big{top:426px;font-size:92px;letter-spacing:1px;}
  .positions{position:absolute;left:0;width:833px;top:577px;text-align:center;font-weight:600;font-size:29.5px;white-space:nowrap;}
  .shifts{position:absolute;top:636px;left:0;width:833px;height:28px;}
  .shift{position:absolute;display:flex;align-items:center;gap:14px;font-size:18px;font-weight:500;}
  .shift svg{width:28px;height:28px;}
  .divider{position:absolute;left:63px;top:695px;width:647px;height:2px;background:var(--teal-line);}
  .bonus{position:absolute;left:0;top:700px;width:833px;height:110px;}
  .bonus-text{position:absolute;left:121px;top:753px;font-family:"Roboto Condensed",sans-serif;font-weight:500;font-size:17px;white-space:nowrap;}
  .bonus-text em{font-style:normal;color:var(--teal-bright);}
  .bonus-amount{position:absolute;left:422px;top:748px;width:76px;text-align:center;font-weight:700;font-size:22px;}
  .bonus-amount small{font-size:13px;}
  .referral{position:absolute;left:529px;top:735px;width:247px;height:62px;border-radius:31px;background:var(--charcoal);}
  .referral-text{position:absolute;left:66px;top:11px;font-family:"Roboto Condensed",sans-serif;font-weight:500;font-size:16px;line-height:1.15;}
  .nurse-photo{position:absolute;left:34px;top:806px;width:236px;height:372px;border-radius:118px 118px 0 0;z-index:2;
    background:linear-gradient(180deg,#2b2b2b 0%,#e6e6e6 30%,#f1f1f1 60%,#9fc6dc 100%);}
  .perks{position:absolute;left:300px;top:0;list-style:none;font-family:"Roboto Condensed",sans-serif;font-weight:500;font-size:17px;}
  .perk{position:absolute;left:0;display:flex;align-items:center;gap:8px;white-space:nowrap;}
  .perk svg{width:20px;height:20px;flex:none;}
  .retirement{position:absolute;left:647px;top:896px;width:100px;height:100px;}
  .retirement-text{position:absolute;left:647px;top:922px;width:100px;text-align:center;line-height:1;}
  .retirement-text b{display:block;font-family:"Montserrat",sans-serif;font-weight:700;font-size:21px;}
  .retirement-text span{display:block;font-family:"Roboto Condensed",sans-serif;font-weight:500;font-size:15px;color:var(--salmon);margin-top:3px;}
  .apply{position:absolute;left:232px;top:1063px;width:560px;height:62px;border-radius:0 31px 31px 0;background:var(--teal-dark);}
  .apply-label{position:absolute;left:78px;top:13px;font-weight:600;font-size:25px;color:var(--teal-bright);white-space:nowrap;}
  .apply-url{position:absolute;left:208px;top:17px;font-weight:600;font-size:20.5px;white-space:nowrap;}
</style>
</head>
<body>
<main class="flyer">
  <div class="hero-photo" role="img" aria-label="Photo of a nurse in green scrubs with arms crossed, stethoscope around the neck, holding a teal balloon"></div>

  <header class="masthead"></header>
  <div class="brand"><span class="brand-mark"></span><span class="brand-name">Brantley Homecare</span></div>
  <div class="masthead-rule"></div>
  <h1>
    <span class="headline headline-small">WE ARE</span>
    <span class="headline headline-big">HIRING</span>
  </h1>

  <h2 class="positions">FULL-TIME and PART-TIME Positions Available</h2>

  <div class="shifts">
    <div class="shift" style="left:86px;">
      <svg viewBox="0 0 28 28"><g fill="var(--salmon)"><circle cx="14" cy="14" r="8"/><g stroke="var(--salmon)" stroke-width="3" stroke-linecap="round"><line x1="14" y1="1.5" x2="14" y2="4"/><line x1="14" y1="24" x2="14" y2="26.5"/><line x1="1.5" y1="14" x2="4" y2="14"/><line x1="24" y1="14" x2="26.5" y2="14"/><line x1="5" y1="5" x2="7" y2="7"/><line x1="21" y1="21" x2="23" y2="23"/><line x1="5" y1="23" x2="7" y2="21"/><line x1="21" y1="7" x2="23" y2="5"/></g></g><circle cx="14" cy="14" r="5" fill="var(--teal)"/></svg>
      <span>days</span>
    </div>
    <div class="shift" style="left:250px;">
      <svg viewBox="0 0 28 28"><path d="M18 3a11 11 0 1 0 7 19A11 11 0 0 1 18 3z" fill="var(--white)"/></svg>
      <span>nights</span>
    </div>
    <div class="shift" style="left:414px;">
      <svg viewBox="0 0 28 28" fill="var(--teal-bright)"><rect x="4" y="6" width="20" height="19" rx="2"/><rect x="8" y="2" width="3" height="6" rx="1"/><rect x="17" y="2" width="3" height="6" rx="1"/><g fill="var(--teal)"><rect x="7" y="12" width="3.5" height="3"/><rect x="12.2" y="12" width="3.5" height="3"/><rect x="17.5" y="12" width="3.5" height="3"/><rect x="7" y="18" width="3.5" height="3"/><rect x="12.2" y="18" width="3.5" height="3"/><rect x="17.5" y="18" width="3.5" height="3"/></g></svg>
      <span>weekdays</span>
    </div>
    <div class="shift" style="left:580px;">
      <svg viewBox="0 0 28 28"><circle cx="14" cy="14" r="12" fill="var(--salmon)"/><circle cx="14" cy="14" r="5" fill="var(--teal)"/><g stroke="var(--teal)" stroke-width="3"><line x1="5.5" y1="5.5" x2="10" y2="10"/><line x1="22.5" y1="5.5" x2="18" y2="10"/><line x1="5.5" y1="22.5" x2="10" y2="18"/><line x1="22.5" y1="22.5" x2="18" y2="18"/></g></svg>
      <span>weekends</span>
    </div>
  </div>

  <div class="divider"></div>

  <svg class="bonus" viewBox="0 0 833 110" aria-hidden="true">
    <path d="M54 43 H430 V88 H54 A14 14 0 0 0 54 43 Z" fill="var(--teal-dark)"/>
    <rect x="74" y="47" width="350" height="37" fill="none" stroke="var(--teal)" stroke-width="3"/>
    <line x1="83" y1="50" x2="83" y2="82" stroke="var(--white)" stroke-width="1.5" stroke-dasharray="2 4"/>
    <line x1="416" y1="50" x2="416" y2="82" stroke="var(--white)" stroke-width="1.5" stroke-dasharray="2 4"/>
    <path d="M226 41 A30 30 0 0 1 279 41" fill="none" stroke="var(--teal-line)" stroke-width="3"/>
    <circle cx="460" cy="63" r="38" fill="var(--teal-dark)"/>
  </svg>
  <p class="bonus-text">SIGN-ON <em>BONUS</em> Programs offered up to</p>
  <p class="bonus-amount"><small>$</small>500</p>

  <div class="referral">
    <svg width="50" height="50" viewBox="0 0 50 50" style="position:absolute;left:4px;top:6px;">
      <circle cx="25" cy="25" r="24" fill="var(--teal)"/>
      <rect x="13" y="16" width="24" height="18" rx="2" fill="var(--white)"/>
      <circle cx="19.5" cy="23" r="3" fill="var(--teal)"/>
      <path d="M15 31 a4.5 4.5 0 0 1 9 0z" fill="var(--teal)"/>
      <rect x="26" y="21" width="8" height="2" fill="var(--teal)"/>
      <rect x="26" y="25" width="8" height="2" fill="var(--teal)"/>
    </svg>
    <p class="referral-text">Refer a Friend<br>BONUS Program</p>
  </div>

  <div class="nurse-photo" role="img" aria-label="Photo of a smiling nurse in a white coat and glasses reading a clipboard"></div>

  <ul class="perks">
    <li class="perk" style="top:812px;"><svg viewBox="0 0 20 20"><circle cx="10" cy="10" r="8.5" fill="none" stroke="var(--teal-bright)" stroke-width="2"/><path d="M6 10.3l2.7 2.7L14 7.5" fill="none" stroke="var(--teal-bright)" stroke-width="2"/></svg>Holiday Pay</li>
    <li class="perk" style="top:842px;"><svg viewBox="0 0 20 20"><circle cx="10" cy="10" r="8.5" fill="none" stroke="var(--teal-bright)" stroke-width="2"/><path d="M6 10.3l2.7 2.7L14 7.5" fill="none" stroke="var(--teal-bright)" stroke-width="2"/></svg>2 Health Plans to Choose from</li>
    <li class="perk" style="top:872px;"><svg viewBox="0 0 20 20"><circle cx="10" cy="10" r="8.5" fill="none" stroke="var(--teal-bright)" stroke-width="2"/><path d="M6 10.3l2.7 2.7L14 7.5" fill="none" stroke="var(--teal-bright)" stroke-width="2"/></svg>Island-Wide Locations</li>
    <li class="perk" style="top:921px;"><svg viewBox="0 0 20 20"><circle cx="10" cy="10" r="8.5" fill="none" stroke="var(--teal-bright)" stroke-width="2"/><path d="M6 10.3l2.7 2.7L14 7.5" fill="none" stroke="var(--teal-bright)" stroke-width="2"/></svg>All PPE Provided (masks, gloves, etc)</li>
    <li class="perk" style="top:950px;"><svg viewBox="0 0 20 20"><circle cx="10" cy="10" r="8.5" fill="none" stroke="var(--teal-bright)" stroke-width="2"/><path d="M6 10.3l2.7 2.7L14 7.5" fill="none" stroke="var(--teal-bright)" stroke-width="2"/></svg>Tuition Benefits</li>
  </ul>

  <svg class="retirement" viewBox="0 0 100 100" aria-hidden="true">
    <defs><clipPath id="ring-clip"><circle cx="50" cy="50" r="47"/></clipPath></defs>
    <circle cx="50" cy="50" r="47" fill="none" stroke="var(--salmon)" stroke-width="3"/>
    <path d="M0 84 Q30 72 55 82 T100 80 V100 H0Z" fill="var(--salmon)" clip-path="url(#ring-clip)"/>
  </svg>
  <p class="retirement-text"><b>401K</b><span>Program</span></p>

  <div class="apply">
    <span class="apply-label">APPLY at</span>
    <span class="apply-url">www.brantleycare.com/jobs</span>
  </div>
</main>
</body>
</html>
```